We need a business card design for a new soccer program based in Melbourne, Victoria, Australia.
Coaching kids from 2 through to 14 develop social, motor and soccer skills, in a fun and friendly non-competitive environment.
Our company colours are blue and orange as seen in the logo attached below. However, we are happy for the font to be any modern colour that looks professional.
Target Market(s)
Mums and dads
Industry/Entity Type
Business
Contact Information for Business Card
business name: Bright Kick Soccer
Marko Delvino Director- 0451 738 015
Luke Ferrano Director- 0419 856 371
Tomas Kovalenko Head Coach
email: marko@brightkicksoccer.com.au
website: www.brightkicksoccer.com.au
Coaching kids from 2-14
https://www.facebook.com/brightkicksoccer (facebook page not required unless it looks good without being clustered)
Look and feel

```html
<!DOCTYPE html>
<html lang="en">
<head>
<meta charset="utf-8">
<title>Bright Kick Soccer – Business Cards</title>
<link rel="stylesheet" href="https://fonts.googleapis.com/css2?family=Roboto+Condensed:wght@300;400;700&display=swap">
<style>
  :root {
    --brand-blue: #2b3289;
    --brand-orange: #ee8a1e;
    --ink-grey: #6d6e71;
    --band-grey: #ececec;
    --card-white: #ffffff;
    --stage: #e4e2df;
    --rule: #b5b5b5;
  }
  * { margin: 0; padding: 0; box-sizing: border-box; }
  html, body {
    width: 1200px; height: 900px; overflow: hidden;
    background: var(--stage);
    font-family: "Roboto Condensed", "Arial Narrow", sans-serif;
  }
  .card {
    position: absolute; left: 270px;
    width: 660px; height: 400px;
    background: var(--card-white);
    overflow: hidden;
    box-shadow: 0 6px 18px rgba(0,0,0,.18);
  }
  .card--front { top: 40px; }
  .card--back { top: 460px; }
  .card__corners { position: absolute; inset: 0; width: 100%; height: 100%; }
  .corner--blue { fill: var(--brand-blue); }
  .corner--orange { fill: var(--brand-orange); }

  .brand {
    position: absolute; display: flex; align-items: center; gap: 14px;
  }
  .brand__dot {
    width: 54px; height: 54px; border-radius: 50%;
    background: var(--brand-orange); flex: none;
  }
  .brand__name {
    color: var(--brand-blue); font-weight: 700;
    font-size: 44px; line-height: .92; text-transform: uppercase;
    letter-spacing: -.5px;
  }
  .card--front .brand { left: 380px; top: 130px; }
  .card--back .brand { left: 320px; top: 60px; }

  .contact { position: absolute; left: 110px; top: 140px; }
  .contact__name {
    font-size: 32px; font-weight: 300; color: var(--ink-grey);
    text-transform: uppercase; letter-spacing: .5px; line-height: 1;
    white-space: nowrap;
  }
  .contact__name strong { color: var(--brand-orange); font-weight: 700; }
  .contact__role {
    font-size: 13px; color: var(--ink-grey); letter-spacing: 1.5px;
    text-transform: uppercase; margin-top: 5px;
  }
  .contact__rule { width: 150px; height: 1px; background: var(--rule); margin: 14px 0; }
  .contact__phone {
    font-size: 26px; font-weight: 700; color: var(--brand-blue); letter-spacing: 1px;
  }

  .tagline-band {
    position: absolute; left: 0; top: 230px; width: 660px; height: 74px;
    background: var(--band-grey);
    display: flex; align-items: center; padding-left: 150px; gap: 12px;
    color: var(--ink-grey); text-transform: uppercase;
  }
  .tagline__lead { display: flex; flex-direction: column; line-height: 1; }
  .tagline__small { font-size: 16px; font-weight: 700; letter-spacing: 1px; }
  .tagline__big { font-size: 42px; font-weight: 300; }
  .tagline__from { font-size: 12px; letter-spacing: 1px; align-self: flex-start; margin-top: 14px; }
  .tagline__ages { font-size: 50px; font-weight: 700; color: #555; line-height: 1; }

  .web-links {
    position: absolute; left: 150px; top: 316px;
    font-size: 17px; line-height: 1.45; color: var(--ink-grey);
  }
  .web-links .site { color: var(--brand-orange); }
  .web-links .site-rule { width: 200px; height: 2px; background: var(--brand-blue); margin-top: 4px; }
</style>
</head>
<body>

<section class="card card--front" aria-label="Business card front">
  <svg class="card__corners" viewBox="0 0 660 400" aria-hidden="true">
    <polygon class="corner--blue" points="510,0 660,0 660,220"/>
    <polygon class="corner--orange" points="0,90 0,400 150,400"/>
  </svg>
  <div class="contact">
    <p class="contact__name"><strong>Marko</strong> Delvino</p>
    <p class="contact__role">Director</p>
    <div class="contact__rule"></div>
    <p class="contact__phone">0451 738 015</p>
  </div>
  <div class="brand">
    <span class="brand__dot"></span>
    <span class="brand__name">Bright<br>Kick<br>Soccer</span>
  </div>
</section>

<section class="card card--back" aria-label="Business card back">
  <svg class="card__corners" viewBox="0 0 660 400" aria-hidden="true">
    <polygon class="corner--blue" points="520,0 660,0 660,190"/>
    <polygon class="corner--orange" points="0,304 0,400 120,400"/>
  </svg>
  <div class="brand">
    <span class="brand__dot"></span>
    <span class="brand__name">Bright<br>Kick<br>Soccer</span>
  </div>
  <div class="tagline-band">
    <div class="tagline__lead">
      <span class="tagline__small">Coaching</span>
      <span class="tagline__big">Kids</span>
    </div>
    <span class="tagline__from">from</span>
    <span class="tagline__ages">2–14</span>
  </div>
  <div class="web-links">
    <p>marko@brightkicksoccer.com.au</p>
    <p class="site">www.brightkicksoccer.com.au</p>
    <div class="site-rule"></div>
  </div>
</section>

</body>
</html>
```